依頼概要
■依頼詳細
弊社が販売する信州産唐辛子ソースの新しいボトルラベルの唐辛子に色付けなどをしていただきたいです。

現状の黒色の唐辛子は印象的で全体のしまり感を醸し出しています。

この印象的でしまり感がある唐辛子に、カブリつきたくなるよう唐辛子が本来もっている、瑞々しさの表現が加えてほしいです。このソースは新鮮な原料しか使っていないので、それをあと一押し表現してほしいです。

※単に唐辛子に光沢をつけるだけでは不採択になると思います。

■新しいラベルデザインについて
この素晴らしいラベルデザインはクリエモールで制作いたしました。
デザイナー様は力を振り絞ってご制作していただけましたが、唐辛子に瑞々しさを表現するところまでは至りませんでした。

■唐辛子の色について
赤色ソースは赤唐辛子、緑ソースは青唐辛子が表現されていることも望ましいです。

・青唐辛子を主原料にした緑色の雅炎香(Amber Blaze:中辛)
・赤唐辛子を主原料にした赤色の雅炎香(Thunder Bite:激辛)

■「雅炎香」の概要
信州産唐辛子100%使用、国産野菜・柑橘果汁を日本人の感性でミックスした無添加無着色の自然派ソース。辛いだけではない、野菜の鮮度と香りが後味豊かに感じられる、これまで世界中どこにも無かった新感覚商品です。

website:miyaenka.jp

■「雅炎香」「Amber Blaze」「Thunder Bite」の意味

和:日本の素材が調和する/日本人の調和を貴ぶ感性が作り上げたソース
美:美味しい
辛:辛いソース

Amber Blaze:女王様のように高貴で優しくても油断できない辛さという意味
Thunder Bite:激しい辛さと美味しさの感動で殺されそうになるという意味

■「雅炎香」のターゲット
食にこだわりがあり、辛い物が好きで、生活の楽しみを向上させる逸品を探している世界中の人々。観光客だけをターゲットにした土産物ではありません。

■ai.データについて

https://17.filecrate.example/0314-a9c3e27d41f08b6e5c92d7a0e4b13f68
からダウンロードお願いします。

使用したデータの控え(pdf)はここに添付します。

・ファイルのデータ著作権は北杜厨房にあります。

■ラベルの仕上がり寸法
幅135㎜ 縦78㎜

■その他要望
その他何かご不明な点がございましたら、お気軽にご質問下さい。

雅炎香は高級百貨店・高質お土産店・国際空港・海外の高質スーパーなど、比較的ハイエンドな市場をターゲットにしています。そのよう市場にふさわしいデザインを求めています。
追記その2
背景の修整よりも、黒い唐辛子が瑞々しくなるように色付けやグラデなどの手法を用いて修正することを優先していただいた方が良いと思います。
唐辛子の形はオファーのまま変えていただかないよう方が良いです。
すみません、私がイメージする唐辛子の言語的な表現が至らずです。
少し考えさせてください。
すみません、唐辛子の色彩的表現と同時に、キャップシールの色の修整もお願いいたします。
報酬UPします。
唐辛子の色彩に合わせてキャップシールラベルの修整もやらないとデザイン的にちぐはぐだと感じました。
諸々の事情のため勝手ながら締切を延長します。
審査は心を込めて厳正に行います。
ご応募いただいた作品は無駄にはしません。
■ 選んだ理由

Ririka様は難しい私の依頼内容を汲み取っていただけました。もともとのデザインの印象的でしまり感がある唐辛子に、カブリつきたくなるよう唐辛子が本来もっている、瑞々しさの表現がなされたと思います。高質土産物店でも十分な存在感を発揮してくるデザインだと思います。

■ 提案者全員のお礼・コメント

今回も、クリエモールの皆様 たくさんのご提案をいただきましてありがとうございました。 クリエモールの皆様が時間とエネルギーをかけて制作していただいたことに感謝申し上げます。 そのことを念頭に置いて、上記の選考理由に沿って心を込めて選考させていただきました。 この度はありがとうございました。 またの機会にもぜひご応募をいただけましたら幸いです。 北杜厨房 森岡

```html
<!DOCTYPE html>
<html lang="ja">
<head>
<meta charset="utf-8">
<title>雅炎香 Chili Pepper Hot Sauce Bottles</title>
<link rel="stylesheet" href="https://fonts.googleapis.com/css2?family=Shippori+Mincho+B1:wght@600;800&family=Playfair+Display:ital,wght@0,700;1,700&display=swap">
<style>
  :root {
    --page: #ffffff;
    --seal: #141210;
    --seal-edge: #2b2622;
    --gold: #c9a45a;
    --gold-deep: #8f6d2c;
    --green-top: #6f9a3a;
    --green-bottom: #2e5218;
    --red-top: #d9452c;
    --red-bottom: #8e1c12;
    --ink: #15120f;
    --white: #ffffff;
    --stamp: #d4231a;
  }
  html, body {
    margin: 0;
    width: 714px;
    height: 1200px;
    overflow: hidden;
    background: var(--page);
  }
  .shelf {
    position: relative;
    width: 714px;
    height: 1200px;
  }
  .bottle {
    position: absolute;
    top: 11px;
    width: 270px;
    height: 1180px;
  }
  .bottle--green { left: 77px; }
  .bottle--red { left: 398px; }
  .jp {
    font-family: "Shippori Mincho B1", serif;
    writing-mode: vertical-rl;
  }
  .origin { font-size: 27px; font-weight: 800; fill: var(--ink); }
  .brand { font-size: 54px; font-weight: 800; fill: var(--ink); letter-spacing: 6px; }
  .heat { font-size: 26px; font-weight: 800; fill: var(--stamp); }
  .note { font-size: 11px; font-weight: 600; fill: var(--white); letter-spacing: 2px; }
  .seal-text { font-size: 13px; font-weight: 600; fill: var(--gold); letter-spacing: 3px; }
  .sub-en {
    font-family: "Playfair Display", serif;
    font-size: 12px;
    font-weight: 700;
    fill: var(--ink);
  }
  .name-en {
    font-family: "Playfair Display", serif;
    font-size: 21px;
    font-weight: 700;
    font-style: italic;
    fill: var(--ink);
  }
  .natural {
    font-family: "Playfair Display", serif;
    font-size: 11px;
    font-weight: 700;
    fill: var(--white);
    letter-spacing: 1px;
  }
</style>
</head>
<body>
<main class="shelf">

  <svg class="bottle bottle--green" viewBox="0 0 270 1180" aria-label="雅炎香 Amber Blaze 中辛">
    <defs>
      <linearGradient id="bodyGreen" x1="0" y1="0" x2="0" y2="1">
        <stop offset="0" stop-color="var(--green-top)"/>
        <stop offset="1" stop-color="var(--green-bottom)"/>
      </linearGradient>
      <linearGradient id="chiliGreen" x1="0" y1="0" x2="1" y2="1">
        <stop offset="0" stop-color="#7fbf3a"/>
        <stop offset="1" stop-color="#2f6a12"/>
      </linearGradient>
      <linearGradient id="goldFade" x1="0" y1="0" x2="1" y2="0">
        <stop offset="0" stop-color="var(--gold)" stop-opacity="0.25"/>
        <stop offset="1" stop-color="var(--gold)" stop-opacity="0.75"/>
      </linearGradient>
    </defs>
    <path class="bottle-body" fill="url(#bodyGreen)"
      d="M75 0 H195 V330 C195 400 270 420 270 500 V1150 Q270 1178 242 1178 H28 Q0 1178 0 1150 V500 C0 420 75 400 75 330 Z"/>
    <path class="cap-seal" fill="var(--seal)"
      d="M75 0 H195 V330 C195 370 222 395 240 420 L30 420 C48 395 75 370 75 330 Z"/>
    <rect class="cap-band" x="75" y="140" width="120" height="50" fill="var(--seal-edge)" stroke="var(--gold)" stroke-width="2"/>
    <rect class="cap-pattern" x="75" y="210" width="120" height="120" fill="url(#goldFade)" role="img" aria-label="金色の文字模様"/>
    <text class="jp seal-text" x="135" y="20">ひりり辛い</text>
    <text class="sub-en" x="161" y="588">Japanese</text>
    <text class="sub-en" x="118" y="604">Chili Pepper Hot Sauce</text>
    <text class="jp note" x="26" y="625">鮮度と香りを</text>
    <text class="jp origin" x="62" y="625">信州産</text>
    <text class="jp origin" x="92" y="625">青唐辛子100%</text>
    <rect class="chili" x="130" y="634" width="60" height="190" rx="30" fill="url(#chiliGreen)" role="img" aria-label="瑞々しい青唐辛子のイラスト"/>
    <text class="jp brand" x="162" y="830">雅炎香</text>
    <rect class="heat-box" x="76" y="890" width="40" height="80" fill="none" stroke="var(--stamp)" stroke-width="3"/>
    <text class="jp heat" x="96" y="900">中辛</text>
    <rect class="gold-mark" x="196" y="612" width="72" height="495" fill="url(#goldFade)" role="img" aria-label="金色の大きな書体装飾"/>
    <text class="name-en" x="100" y="1080" text-anchor="middle">“Amber Blaze”</text>
    <text class="natural" x="100" y="1106" text-anchor="middle">ALL NATURAL</text>
  </svg>

  <svg class="bottle bottle--red" viewBox="0 0 270 1180" aria-label="雅炎香 Thunder Bite 激辛">
    <defs>
      <linearGradient id="bodyRed" x1="0" y1="0" x2="0" y2="1">
        <stop offset="0" stop-color="var(--red-top)"/>
        <stop offset="1" stop-color="var(--red-bottom)"/>
      </linearGradient>
      <linearGradient id="chiliRed" x1="0" y1="0" x2="1" y2="1">
        <stop offset="0" stop-color="#f0442a"/>
        <stop offset="1" stop-color="#7e0e08"/>
      </linearGradient>
      <linearGradient id="goldFadeRed" x1="0" y1="0" x2="1" y2="0">
        <stop offset="0" stop-color="var(--gold)" stop-opacity="0.25"/>
        <stop offset="1" stop-color="var(--gold)" stop-opacity="0.75"/>
      </linearGradient>
    </defs>
    <path class="bottle-body" fill="url(#bodyRed)"
      d="M75 0 H195 V330 C195 400 270 420 270 500 V1150 Q270 1178 242 1178 H28 Q0 1178 0 1150 V500 C0 420 75 400 75 330 Z"/>
    <path class="cap-seal" fill="var(--seal)"
      d="M75 0 H195 V330 C195 370 222 395 240 420 L30 420 C48 395 75 370 75 330 Z"/>
    <rect class="cap-band" x="75" y="140" width="120" height="50" fill="var(--seal-edge)" stroke="var(--gold)" stroke-width="2"/>
    <rect class="cap-pattern" x="75" y="210" width="120" height="120" fill="url(#goldFadeRed)" role="img" aria-label="金色の文字模様"/>
    <text class="jp seal-text" x="135" y="20">ひりり辛い</text>
    <text class="sub-en" x="161" y="588">Japanese</text>
    <text class="sub-en" x="118" y="604">Chili Pepper Hot Sauce</text>
    <text class="jp note" x="26" y="625">素材を大切に</text>
    <text class="jp origin" x="62" y="625">信州産</text>
    <text class="jp origin" x="92" y="625">赤唐辛子100%</text>
    <rect class="chili" x="130" y="634" width="60" height="190" rx="30" fill="url(#chiliRed)" role="img" aria-label="瑞々しい赤唐辛子のイラスト"/>
    <text class="jp brand" x="162" y="830">雅炎香</text>
    <rect class="heat-box" x="76" y="890" width="40" height="80" fill="var(--white)" stroke="var(--stamp)" stroke-width="3"/>
    <text class="jp heat" x="96" y="900">激辛</text>
    <rect class="gold-mark" x="196" y="612" width="72" height="495" fill="url(#goldFadeRed)" role="img" aria-label="金色の大きな書体装飾"/>
    <text class="name-en" x="100" y="1080" text-anchor="middle">“Thunder Bite”</text>
    <text class="natural" x="100" y="1106" text-anchor="middle">ALL NATURAL</text>
  </svg>

</main>
</body>
</html>
```